Commercial Real Estate Company Needs Website Redesign

Velmarco is a commercial real estate firm that is based in San Diego, but has offices and properties across the U.S. The current website was completed almost 3 years ago and is need of a refresh. We will rework the existing Wordpress CMS system, but require a new design. We have a great programmer who can take the design into wordpress. I need a design template for each page types, There are are approximately 20 pages for each section of our site. There are 4 Sections: Corporate, Hospitality, Commercial/Residential, and Receiver/Bankruptcy. See attached creative brief for the initial pages we would like drafted.

Industry/Entity Type

Real Estate

```html
<!DOCTYPE html>
<html lang="en">
<head>
<meta charset="utf-8">
<title>Velmarco – Commercial Real Estate</title>
<link href="https://fonts.googleapis.com/css2?family=Roboto:wght@300;400;500;700;900&family=Roboto+Condensed:wght@700&display=swap" rel="stylesheet">
<style>
:root{
  --navy:#0f1a2e;
  --navy-footer:#17284a;
  --orange:#f39a24;
  --orange-light:#f7b04a;
  --white:#ffffff;
  --ink:#1b2233;
  --grey-text:#7d879c;
  --client-grey:#5a5a5a;
}
*{box-sizing:border-box;margin:0;padding:0}
html,body{width:965px;height:1200px;overflow:hidden;background:var(--white)}
body{position:relative;font-family:'Roboto',Arial,sans-serif;color:var(--ink)}
.abs{position:absolute}

/* hero */
.hero{left:0;top:0;width:965px;height:304px;
  background:linear-gradient(180deg,#6a9fd0 0%,#b9cde0 30%,#d9c7a6 55%,#8a7a5a 78%,#3b4a3a 100%)}
.site-header{left:70px;top:0;width:835px;height:63px;background:rgba(15,26,46,.93);
  clip-path:polygon(0 0,100% 0,97% 100%,3% 100%)}
.brand{left:118px;top:19px;color:var(--white)}
.brand-name{display:flex;align-items:center;gap:6px;font-weight:500;font-size:25px;letter-spacing:1px;line-height:1}
.brand-mark{width:12px;height:12px;background:var(--orange)}
.nav a{position:absolute;top:28px;font-size:11px;color:var(--white);text-decoration:none;white-space:nowrap}
.nav .current{color:var(--orange)}
.nav .caret{position:absolute;left:50%;top:16px;width:6px;height:4px;margin-left:-3px}
.nav .boxed{top:22px;border:1.5px solid var(--white);padding:5px 7px}
.call{left:744px;top:16px;color:var(--white);white-space:nowrap}
.call small{display:flex;align-items:center;gap:3px;font-size:7px;letter-spacing:.3px;padding-left:10px}
.call b{display:block;font-weight:400;font-size:11px;color:var(--orange);margin-top:3px}
.divider{left:816px;top:18px;width:1px;height:26px;background:#55607a}
.social{top:24px;width:10px;height:10px;border-radius:50%;background:var(--white)}
.slide-caption{left:0;top:267px;width:965px;text-align:center;font-weight:500;font-size:25px;color:var(--white);text-shadow:0 1px 3px rgba(0,0,0,.5)}
.slide-arrow{top:271px}

/* dark band */
.dark-band{left:0;top:304px;width:965px;height:330px;background:var(--navy)}
.newsletter{left:58px;top:304px;width:847px;height:61px;background:var(--orange);
  clip-path:polygon(0 0,100% 0,94% 100%,6% 100%)}
.newsletter-label{left:200px;top:327px;font-size:16px;font-weight:300;color:var(--ink)}
.field{top:325px;height:23px;background:var(--navy);color:#c9cfdb;font-style:italic;font-size:10.5px;padding:5px 7px}
.subscribe{left:661px;top:325px;width:102px;height:23px;border:1.5px solid var(--navy);font-size:10px;font-weight:700;text-align:center;line-height:20px;color:var(--navy)}
.audience{top:391px;width:222px;text-align:center}
.audience h3{font-weight:300;font-size:17px;color:var(--white)}
.audience h3 b{font-weight:500}
.audience .photo{width:222px;height:97px;margin-top:16px}
.audience p{margin-top:17px;font-size:9.5px;line-height:15.5px;color:var(--grey-text);padding:0 6px}

/* about */
.about{left:0;top:634px;width:965px;height:192px;
  background:linear-gradient(135deg,var(--orange-light),var(--orange) 60%,#ee9120);
  clip-path:polygon(0 0,100% 0,100% 69%,93% 100%,7% 100%,0 69%)}
.about h2{position:absolute;left:0;top:20px;width:965px;text-align:center;font-family:'Roboto Condensed',Arial,sans-serif;font-size:31px;color:var(--white)}
.about p{position:absolute;left:108px;top:63px;width:750px;text-align:center;font-size:13.2px;line-height:19px;color:var(--ink)}

/* clients */
.clients-title{left:0;top:846px;width:965px;text-align:center;font-family:'Roboto Condensed',Arial,sans-serif;font-size:33px;color:var(--navy)}
.client{top:922px;height:30px;display:flex;align-items:center;justify-content:center;gap:8px;font-weight:700;font-size:22px;color:var(--client-grey);white-space:nowrap}
.client i{display:block;width:20px;height:20px;border-radius:50%;background:var(--client-grey)}
.client-arrow{top:931px}
.cta{left:114px;top:1024px;width:735px;height:43px;border:2px solid var(--orange);display:flex;align-items:center;font-weight:300;font-size:25px;color:var(--ink)}
.cta .cta-text{margin-left:62px}
.cta .cta-phone{margin-left:46px;display:flex;align-items:center;gap:10px}

/* footer */
.site-footer{left:0;top:1103px;width:965px;height:97px;background:var(--navy-footer)}
.footer-brand{left:116px;top:1124px;color:var(--white)}
.footer-address{left:151px;top:1174px;font-size:8px;line-height:11px;color:#5d6d90}
.footer-links{left:560px;top:1131px;width:289px;text-align:right;font-size:8px;line-height:10.5px;color:var(--white)}
.footer-links .active{color:#7f8db0}
.copyright{left:600px;top:1177px;width:249px;text-align:right;font-size:8px;letter-spacing:1px;color:#5d6d90}
</style>
</head>
<body>

<div class="abs hero" role="img" aria-label="Photo of a resort hotel with palm trees and a wooden footbridge over a pool"></div>

<header>
  <div class="abs site-header"></div>
  <div class="abs brand">
    <div class="brand-name"><span class="brand-mark"></span>VELMARCO</div>
  </div>
  <nav class="nav">
    <a class="current" style="left:312px">Who we are<svg class="caret" viewBox="0 0 6 4"><path d="M0 0l3 3 3-3" fill="none" stroke="#f39a24" stroke-width="1.2"/></svg></a>
    <a style="left:394px">What we do<svg class="caret" viewBox="0 0 6 4"><path d="M0 0l3 3 3-3" fill="none" stroke="#fff" stroke-width="1.2"/></svg></a>
    <a style="left:477px">What we've done<svg class="caret" viewBox="0 0 6 4"><path d="M0 0l3 3 3-3" fill="none" stroke="#fff" stroke-width="1.2"/></svg></a>
    <a class="boxed" style="left:575px">Contact us</a>
    <a style="left:658px">Velmarco home</a>
  </nav>
  <div class="abs call">
    <small><svg width="8" height="8" viewBox="0 0 24 24"><path d="M6.6 10.8a15 15 0 0 0 6.6 6.6l2.2-2.2c.3-.3.7-.4 1-.2 1.1.4 2.3.6 3.6.6.6 0 1 .4 1 1V20c0 .6-.4 1-1 1A17 17 0 0 1 3 4c0-.6.4-1 1-1h3.5c.6 0 1 .4 1 1 0 1.3.2 2.5.6 3.6.1.3 0 .7-.2 1z" fill="#fff"/></svg>CALL TODAY</small>
    <b>555-318-4470</b>
  </div>
  <div class="abs divider"></div>
  <span class="abs social" style="left:825px"></span>
  <span class="abs social" style="left:842px"></span>
</header>

<svg class="abs slide-arrow" style="left:116px" width="14" height="26" viewBox="0 0 14 26"><path d="M12 2L2 13l10 11" fill="none" stroke="#fff" stroke-width="2.5"/></svg>
<div class="abs slide-caption">Contact us Today! Let us put our expertise to work for you</div>
<svg class="abs slide-arrow" style="left:836px" width="14" height="26" viewBox="0 0 14 26"><path d="M2 2l10 11L2 24" fill="none" stroke="#fff" stroke-width="2.5"/></svg>

<section>
  <div class="abs dark-band"></div>
  <div class="abs newsletter"></div>
  <div class="abs newsletter-label">Subscribe to our newsletter</div>
  <div class="abs field" style="left:406px;width:121px">Your Name...</div>
  <div class="abs field" style="left:533px;width:122px">Email Address...</div>
  <div class="abs subscribe">SUBSCRIBE NOW!</div>

  <div class="abs audience" style="left:113px">
    <h3>For <b>Owners</b></h3>
    <div class="photo" role="img" aria-label="Photo of a grand hotel lobby with seating and a curved staircase" style="background:linear-gradient(160deg,#c99a5a,#7a4a22 60%,#3a2210)"></div>
    <p>Since 1976, Velmarco has managed full range of hotels, delivering top notch results through a full range of onsite service. From urban city center airport hotels to historic properties to exclusive retreats and resorts.</p>
  </div>
  <div class="abs audience" style="left:371px">
    <h3>For <b>Buyers/Developers</b></h3>
    <div class="photo" role="img" aria-label="Photo of a high-rise building under construction with cranes" style="background:linear-gradient(180deg,#3f7fd6,#8fb3de 45%,#6d7a8a)"></div>
    <p>With Aggressive sales efforts, revenue management expertise, and disciplined expenses controls. Velmarco's operations team is strategically located throughout the country and offers a turnkey approach.</p>
  </div>
  <div class="abs audience" style="left:627px">
    <h3>For <b>Lenders</b></h3>
    <div class="photo" role="img" aria-label="Photo of a handshake closing a business deal" style="background:linear-gradient(135deg,#7a3a1e,#d9a47a 50%,#e8c6a6)"></div>
    <p>Whether through receivership or REO, Velmarco is able to lenders and special servicers revive distressed and performing hotels and Consistently outperform industry benchmarks.</p>
  </div>
</section>

<section class="abs about">
  <h2>ABOUT VELMARCO</h2>
  <p>Velmarco is a fully integrated commercial real estate management, fiduciary and advisory firm. Leveraging over 38 years of experience in varying economic climates, we provide our clients with outstanding performance and unmatched integrity. We have expertise in the commercial real estate, hospitality and petroleum industries, bringing our broad range of experience and depth of knowledge to every assignment. Whether we are building value through management for investors or solving complex problems for lenders, attorneys and the courts, you can count on Velmarco to maximize value.</p>
</section>

<section>
  <h2 class="abs clients-title">OUR CLIENTS</h2>
  <svg class="abs client-arrow" style="left:113px" width="20" height="20" viewBox="0 0 20 20"><rect x="1" y="1" width="18" height="18" rx="3" fill="none" stroke="#444" stroke-width="1.3"/><path d="M14 10H6m3-3l-3 3 3 3" fill="none" stroke="#444" stroke-width="1.3"/></svg>
  <div class="abs client" style="left:148px;width:124px"><i></i>Norvane</div>
  <div class="abs client" style="left:288px;width:122px">Crestline</div>
  <div class="abs client" style="left:468px;width:124px">Harborview</div>
  <div class="abs client" style="left:646px;width:139px">Alveron</div>
  <svg class="abs client-arrow" style="left:831px" width="20" height="20" viewBox="0 0 20 20"><rect x="1" y="1" width="18" height="18" rx="3" fill="none" stroke="#444" stroke-width="1.3"/><path d="M6 10h8m-3-3l3 3-3 3" fill="none" stroke="#444" stroke-width="1.3"/></svg>

  <div class="abs cta">
    <span class="cta-text">CALL FOR A FREE CONSULTATION</span>
    <span class="cta-phone">
      <svg width="20" height="20" viewBox="0 0 24 24"><path d="M6.6 10.8a15 15 0 0 0 6.6 6.6l2.2-2.2c.3-.3.7-.4 1-.2 1.1.4 2.3.6 3.6.6.6 0 1 .4 1 1V20c0 .6-.4 1-1 1A17 17 0 0 1 3 4c0-.6.4-1 1-1h3.5c.6 0 1 .4 1 1 0 1.3.2 2.5.6 3.6.1.3 0 .7-.2 1z" fill="none" stroke="#f39a24" stroke-width="1.6"/><path d="M14 3a7 7 0 0 1 7 7M14 6.5a3.5 3.5 0 0 1 3.5 3.5" fill="none" stroke="#f39a24" stroke-width="1.6"/></svg>
      555-318-4470
    </span>
  </div>
</section>

<footer>
  <div class="abs site-footer"></div>
  <div class="abs brand footer-brand">
    <div class="brand-name"><span class="brand-mark"></span>VELMARCO</div>
  </div>
  <div class="abs footer-address">Velmarco • 4120 Larkspur Way Suite 210 • San Diego, California 92108<br>Tel: 1.555.318.4470 • Fax: 1.555.318.4471</div>
  <div class="abs footer-links">
    Home &nbsp;|&nbsp; Property Management Receivership &amp; Bankruptcy &nbsp;|<br>
    Lender Conference &nbsp;|&nbsp; Success Stories &nbsp;|&nbsp; <span class="active">About Velmarco</span> &nbsp;|&nbsp; Media Room &nbsp;|<br>
    Contact Us &nbsp;|&nbsp; Careers at Velmarco &nbsp;|&nbsp; Email &nbsp;|&nbsp; Login
  </div>
  <div class="abs copyright">© 2013 Velmarco, All Rights Reserved.</div>
</footer>

</body>
</html>
```